Stationery design for Kelvorine Holdings Nig Ltd
Kelvorine holdings Nig ltd
Stationery design for Kelvorine Holdings Nig Ltd - Real Estate
Creative Brief
Tobias Emeka Lunsford
Executive Director, Business Dev & Marketing
Plot 27, Mossgate Road Opp. Brindley Gardens Mossgate Jos Plateau State
telunsford@kelvorineltd.com
www.kelvorineltd.com
We like uncluttered design. pls NO rooftops. try to de-emphasize the 'commodities' in our name as much as possible
should contain our logo and tagline: With us, time is on your side.

```html
<!DOCTYPE html>
<html lang="en">
<head>
<meta charset="utf-8">
<title>Kelvorine Holdings Nig Ltd – Business Card</title>
<link href="https://fonts.googleapis.com/css2?family=Open+Sans:ital,wght@0,400;0,600;0,700;1,400&display=swap" rel="stylesheet">
<style>
  :root {
    --bg: #e9eaec;
    --card-dark: #2a2a2c;
    --card-dark-2: #141415;
    --orange: #f26a12;
    --orange-light: #ffa21f;
    --green: #5da42f;
    --green-dark: #3f7f1f;
    --gold: #e0a722;
    --white: #ffffff;
    --ink: #2b1a0d;
  }
  * { margin: 0; padding: 0; box-sizing: border-box; }
  html, body { width: 1200px; height: 993px; overflow: hidden; }
  body {
    background: var(--bg);
    font-family: "Open Sans", sans-serif;
    position: relative;
  }
  .card {
    position: absolute;
    width: 620px;
    height: 354px;
    border-radius: 22px;
    overflow: hidden;
    box-shadow: 0 10px 30px rgba(0,0,0,0.18);
  }
  /* Back side */
  .card-back {
    left: 500px; top: 110px;
    background: radial-gradient(ellipse at 50% 30%, var(--card-dark) 0%, var(--card-dark-2) 90%);
  }
  .back-mark {
    position: absolute; left: 0; right: 0; top: 98px;
    display: flex; align-items: center; justify-content: center; gap: 16px;
  }
  .mark-dot {
    width: 64px; height: 64px; border-radius: 50%;
    background: var(--gold);
  }
  .back-name {
    color: var(--white); font-weight: 700; font-size: 40px; letter-spacing: 0.5px;
  }
  .back-tagline {
    position: absolute; left: 0; right: 0; top: 212px;
    text-align: center; color: var(--orange);
    font-weight: 700; font-size: 20px; letter-spacing: 3px; text-transform: uppercase;
  }
  /* Front side */
  .card-front {
    left: 80px; top: 520px;
    background: linear-gradient(180deg, var(--card-dark) 0%, var(--card-dark-2) 100%);
  }
  .front-waves { position: absolute; inset: 0; width: 100%; height: 100%; }
  .front-mark {
    position: absolute; left: 30px; top: 30px;
    display: flex; align-items: center; gap: 12px;
  }
  .front-mark .mark-dot { width: 46px; height: 46px; }
  .front-name { color: var(--white); font-weight: 700; font-size: 34px; }
  .front-tagline {
    position: absolute; left: 32px; top: 86px;
    color: var(--green); font-size: 9px; font-weight: 600;
    letter-spacing: 1.6px; text-transform: uppercase;
  }
  .person {
    position: absolute; right: 30px; top: 58px; text-align: right; color: var(--white);
  }
  .person-name { font-size: 19px; font-weight: 600; }
  .person-title { font-size: 10.5px; font-style: italic; margin-top: 3px; }
  .contact {
    position: absolute; right: 30px; top: 186px;
    list-style: none; text-align: right; color: var(--ink);
    font-size: 11.5px; line-height: 1.5;
  }
  .contact li { display: flex; justify-content: flex-end; align-items: center; gap: 8px; }
  .contact svg { width: 11px; height: 11px; flex: none; }
  .spacer { width: 11px; flex: none; }
</style>
</head>
<body>

<section class="card card-back" aria-label="Business card back">
  <div class="back-mark">
    <span class="mark-dot"></span>
    <span class="back-name">Kelvorine</span>
  </div>
  <p class="back-tagline">With us, time is on your side</p>
</section>

<section class="card card-front" aria-label="Business card front">
  <svg class="front-waves" viewBox="0 0 620 354" preserveAspectRatio="none" aria-hidden="true">
    <defs>
      <linearGradient id="orangeFill" x1="0" y1="1" x2="1" y2="0">
        <stop offset="0" stop-color="#f58a16"/>
        <stop offset="0.55" stop-color="#ff9d1e"/>
        <stop offset="1" stop-color="#f05a10"/>
      </linearGradient>
      <linearGradient id="greenFill" x1="0" y1="0" x2="1" y2="0">
        <stop offset="0" stop-color="#3f7f1f"/>
        <stop offset="0.5" stop-color="#6fb83a"/>
        <stop offset="1" stop-color="#3f7f1f"/>
      </linearGradient>
    </defs>
    <path d="M0 118 C160 110 260 200 400 160 C500 130 560 120 620 128 L620 354 L0 354 Z" fill="url(#greenFill)"/>
    <path d="M0 140 C160 128 260 222 400 182 C500 152 560 148 620 156 L620 354 L0 354 Z" fill="url(#orangeFill)"/>
  </svg>

  <div class="front-mark">
    <span class="mark-dot"></span>
    <span class="front-name">Kelvorine</span>
  </div>
  <p class="front-tagline">With us, time is on your side</p>

  <div class="person">
    <p class="person-name">Tobias Emeka Lunsford</p>
    <p class="person-title">Executive Director Business Dev &amp; Marketing</p>
  </div>

  <ul class="contact">
    <li>Plot 27, Mossgate Road<span class="spacer"></span></li>
    <li>Opp. Brindley Gardens<span class="spacer"></span></li>
    <li>Mossgate Jos. Plateau State
      <svg viewBox="0 0 12 12"><path d="M6 0.5a4 4 0 0 0-4 4c0 3 4 7 4 7s4-4 4-7a4 4 0 0 0-4-4z" fill="#2b1a0d"/><circle cx="6" cy="4.5" r="1.5" fill="#ffa21f"/></svg></li>
    <li>+2348055512047
      <svg viewBox="0 0 12 12"><path d="M3 1l2 2.5-1.2 1.3a7 7 0 0 0 3.4 3.4L8.5 7 11 9l-1.3 2C5 11 1 7 1 2.3z" fill="#2b1a0d"/></svg></li>
    <li>+2348069930418<span class="spacer"></span></li>
    <li>telunsford@kelvorineltd.com
      <svg viewBox="0 0 12 12"><rect x="0.5" y="2" width="11" height="8" rx="1" fill="#2b1a0d"/><path d="M1 3l5 4 5-4" stroke="#ffa21f" fill="none"/></svg></li>
    <li>www.kelvorineltd.com
      <svg viewBox="0 0 12 12"><circle cx="6" cy="6" r="5" fill="none" stroke="#2b1a0d" stroke-width="1.3"/><path d="M1 6h10M6 1c-2.5 3-2.5 7 0 10M6 1c2.5 3 2.5 7 0 10" stroke="#2b1a0d" fill="none"/></svg></li>
  </ul>
</section>

</body>
</html>
```